Bref créative |
BrightMoor Guard, LLC. | ||
Use standard fonts | ||
Cutting-Edge Modern Simple |
Derek Palvane | ||
Master Technician | ||
leave blank | ||
brightmooritllc@quellmail.example | ||
http://brightmoorguard.example | ||

```html
<!DOCTYPE html>
<html lang="en">
<head>
<meta charset="utf-8">
<title>BrightMoor Guard, LLC. — Business Card</title>
<link rel="stylesheet" href="https://fonts.googleapis.com/css2?family=Cinzel:wght@500;600&family=Open+Sans:wght@400;600;700&display=swap">
<style>
  :root {
    --stage: #3a3a3c;
    --card: #ffffff;
    --card-edge: #e4e6ea;
    --brand-blue: #1f4fa3;
    --label-blue: #2a5fb8;
    --ink: #2b2b2b;
    --muted: #6d6f73;
  }
  * { margin: 0; padding: 0; box-sizing: border-box; }
  html, body {
    width: 1200px; height: 720px; overflow: hidden;
    background: var(--stage);
  }
  .canvas {
    width: 1200px; height: 720px;
    display: flex; align-items: center; justify-content: center; gap: 50px;
  }
  .card {
    width: 525px; height: 300px;
    background: var(--card);
    border-radius: 14px;
    border: 1px solid var(--card-edge);
    position: relative;
    box-shadow: 0 10px 26px rgba(0,0,0,0.35);
    overflow: hidden;
  }
  /* back side */
  .card-back {
    display: flex; flex-direction: column; align-items: center; justify-content: center;
  }
  .back-mark { width: 150px; height: 150px; }
  .back-name {
    margin-top: 18px;
    font-family: "Cinzel", serif; font-weight: 600;
    font-size: 20px; letter-spacing: 1px; color: var(--brand-blue);
  }
  .back-url {
    margin-top: 10px;
    font-family: "Open Sans", sans-serif; font-size: 11px;
    letter-spacing: 2px; color: var(--muted);
  }
  /* front side */
  .front-brand {
    position: absolute; top: 34px; left: 0; right: 0;
    display: flex; flex-direction: column; align-items: center;
  }
  .front-mark { width: 62px; height: 62px; }
  .company-name {
    margin-top: 12px;
    font-family: "Cinzel", serif; font-weight: 600;
    font-size: 21px; color: var(--ink); letter-spacing: 0.5px;
  }
  .company-tagline {
    margin-top: 2px;
    font-family: "Cinzel", serif; font-weight: 500;
    font-size: 12px; color: var(--ink); letter-spacing: 1px;
  }
  .contact-person {
    position: absolute; right: 32px; top: 150px; text-align: right;
    font-family: "Open Sans", sans-serif;
  }
  .person-name { font-size: 15px; font-weight: 700; color: var(--label-blue); }
  .person-title { margin-top: 6px; font-size: 10px; color: var(--muted); }
  .contact-lines {
    position: absolute; left: 30px; bottom: 34px;
    font-family: "Open Sans", sans-serif; font-size: 11px; color: var(--muted);
    line-height: 1.9;
  }
  .contact-label { font-weight: 700; color: var(--label-blue); }
</style>
</head>
<body>
<main class="canvas">
  <section class="card card-back" aria-label="Card back">
    <svg class="back-mark" viewBox="0 0 150 150" aria-hidden="true">
      <circle cx="75" cy="75" r="75" fill="#1f4fa3"/>
    </svg>
    <p class="back-name">BrightMoor Guard</p>
    <p class="back-url">www.brightmoorguard.example</p>
  </section>

  <section class="card card-front" aria-label="Card front">
    <div class="front-brand">
      <svg class="front-mark" viewBox="0 0 62 62" aria-hidden="true">
        <circle cx="31" cy="31" r="31" fill="#1f4fa3"/>
      </svg>
      <h1 class="company-name">BRIGHTMOOR GUARD, LLC.</h1>
      <p class="company-tagline">AN IT SOLUTIONS FIRM.</p>
    </div>
    <div class="contact-person">
      <p class="person-name">Derek Palvane</p>
      <p class="person-title">Master Technician</p>
    </div>
    <div class="contact-lines">
      <p><span class="contact-label">Web :</span> (555) 014-2278</p>
      <p><span class="contact-label">E-mail :</span> brightmooritllc@quellmail.example</p>
    </div>
  </section>
</main>
</body>
</html>
```